Updated Dealer Toolbox- Marketing

We need a post card that is marketing a new online resource that is available on our website. This is a Toolbox, which contains many helpful tools and downloads to our clients. We need this post card to have 4 main bullet points on the front, with the logo of our resource toolbox, and on the back- our contact information and how to register.We work in dealerships across the USA that are part of the Outdoor Power Industry (mowers, farm equipment, etc) We would like this to be a classy but easy to read format, as our clients are busy and need to get the point quickly.

My personal contact information: Delphine@tomwarbury.net. 555-213-9086
Updates

i have added additional files, and will be adding the logo today. Sorry for the lack of information. Added Wednesday, May 6, 2015

Industry/Entity Type

Marketing

Font styles to use
Serif

Requirements
Must have
• Toolbox attachment on front, contact info on back
Nice to have
• Colors that will attract the eye in the mail
Should not have
• Additional text or designs. Just what is submitted

```html
<!DOCTYPE html>
<html lang="en">
<head>
<meta charset="utf-8">
<title>What's in the Toolbox? – Postcard</title>
<link rel="stylesheet" href="https://fonts.googleapis.com/css2?family=Sorts+Mill+Goudy&display=swap">
<style>
  :root {
    --green-deep: #0c2a22;
    --green-mid: #1f5a48;
    --green-glow: #2f7660;
    --banner-red: #c4161c;
    --banner-red-dark: #8e0f13;
    --toolbox-red: #d42026;
    --toolbox-shade: #7a0d10;
    --ink-white: #ffffff;
    --band-white: #f7f8f6;
    --band-grey: #e2e5e2;
    --brand-green: #1d4d3c;
  }
  * { margin: 0; padding: 0; box-sizing: border-box; }
  html, body { width: 1200px; height: 930px; overflow: hidden; }
  body { font-family: "Sorts Mill Goudy", "Goudy Old Style", Georgia, serif; }

  .postcard {
    position: relative;
    width: 1200px;
    height: 930px;
    background:
      radial-gradient(ellipse 70% 55% at 55% 30%, var(--green-glow) 0%, var(--green-mid) 40%, var(--green-deep) 100%);
    overflow: hidden;
  }

  .toolbox-art {
    position: absolute;
    left: 45px;
    top: 248px;
    width: 650px;
    height: 462px;
    border-radius: 10px;
    background: linear-gradient(160deg, var(--toolbox-red) 0%, var(--toolbox-shade) 70%, #d9dcda 100%);
  }

  .headline-banner {
    position: absolute;
    left: 683px;
    top: 255px;
    width: 517px;
    height: 128px;
    background: linear-gradient(180deg, var(--banner-red) 0%, var(--banner-red-dark) 100%);
    box-shadow: 0 4px 10px rgba(0,0,0,0.35);
  }
  .headline {
    color: var(--ink-white);
    font-weight: 400;
    font-size: 60px;
    line-height: 56px;
    padding-top: 8px;
  }
  .headline span { display: block; }
  .headline .line-one { padding-left: 22px; }
  .headline .line-two { padding-left: 97px; }

  .tool-list {
    position: absolute;
    left: 698px;
    top: 392px;
    list-style: none;
    color: var(--ink-white);
    font-size: 48px;
    line-height: 69px;
    letter-spacing: 0.5px;
  }
  .tool-list li::before { content: "•"; margin-right: 4px; }

  .footer-band {
    position: absolute;
    left: 0;
    top: 772px;
    width: 1200px;
    height: 158px;
    background: linear-gradient(180deg, var(--band-white) 0%, var(--band-grey) 100%);
    border-top: 3px solid var(--green-deep);
  }
  .web-address {
    position: absolute;
    left: 52px;
    top: 56px;
    color: var(--brand-green);
    font-size: 45px;
  }
  .brand-mark {
    position: absolute;
    left: 862px;
    top: 38px;
    display: flex;
    align-items: center;
    gap: 14px;
  }
  .brand-mark .brand-square {
    width: 58px;
    height: 58px;
    background: var(--brand-green);
  }
  .brand-mark .brand-name {
    color: var(--brand-green);
    font-size: 30px;
    line-height: 34px;
  }
</style>
</head>
<body>
  <main class="postcard">
    <div class="toolbox-art" role="img" aria-label="Red toolbox with the word TOOLS rising from it, beside a white computer mouse"></div>

    <div class="headline-banner">
      <h1 class="headline">
        <span class="line-one">What’s in</span>
        <span class="line-two">the Toolbox?</span>
      </h1>
    </div>

    <ul class="tool-list">
      <li>Webinars</li>
      <li>Job Descriptions</li>
      <li>Rental Forms</li>
      <li>Audio Podcasts</li>
    </ul>

    <footer class="footer-band">
      <p class="web-address">www.tomwarbury.net</p>
      <div class="brand-mark">
        <div class="brand-square"></div>
        <p class="brand-name">Tom Warbury<br>International, Inc.</p>
      </div>
    </footer>
  </main>
</body>
</html>
```